New digital business consulting firm needs a professional Wordpress site

Lanternby Works Inc. is a new consulting firm that helps large companies with Digital Transformation. We help companies define a digital transformation strategy for improving the products, processes and customer journey using digital technology.

The website will serve three purposes:
1) Represent what the firm does.
2) Allow people to download research reports.
3) Collect email addresses from people who my be interested in using our services.

The tone of the website should be innovative and professional. The website will have only a few pages. You can see the type of content we wish to post on the current website www.lanternbyworks.example.

The website will support a book that is about to be released. The book cover is attached. However, the website does not necessarily have to match the book cover. Do not be constrained by the book cover.

Target Market(s)

Executives in large companies

Industry/Entity Type

Management Consulting

Font styles to use
Sans Serif

Requirements
Must have
• Professional and innovative, clean, cool
Nice to have
• None
Should not have
• None

```html
<!DOCTYPE html>
<html lang="en">
<head>
<meta charset="utf-8">
<title>Lanternby Works Inc. — Homepage</title>
<link href="https://fonts.googleapis.com/css2?family=Barlow+Condensed:wght@500;600;700&family=Raleway:wght@400;500;600&display=swap" rel="stylesheet">
<style>
:root{
  --navy:#12235c;
  --navy-deep:#0b1640;
  --footer:#0e1c4f;
  --green:#7a9a3d;
  --green-dark:#6a8733;
  --yellow:#fbe5a0;
  --cream:#fbf4d8;
  --ink:#2b2b2b;
  --text:#555;
  --muted:#888;
  --line:#e3e3e3;
  --field:#ededed;
  --alert:#e21b1b;
  --white:#fff;
}
*{box-sizing:border-box;margin:0;padding:0}
html,body{width:1200px;height:3571px;overflow:hidden;background:var(--white)}
body{font-family:"Raleway",Arial,sans-serif;color:var(--text);position:relative}
.cond{font-family:"Barlow Condensed","Arial Narrow",sans-serif}

/* presentation labels */
.board-label{position:absolute;left:0;width:1200px;text-align:center;font-family:"Barlow Condensed","Arial Narrow",sans-serif;font-weight:600;color:var(--ink);letter-spacing:1px}
.board-label--top{top:8px;font-size:38px;line-height:40px}
.board-arrow{position:absolute;left:592px;top:92px}
.board-label--home{top:862px;font-size:38px;line-height:48px}

/* hero */
.hero{position:absolute;left:0;width:1200px;overflow:hidden}
.hero--showcase{top:131px;height:702px;outline:7px solid var(--alert);outline-offset:-7px}
.hero--home{top:929px;height:714px}
.hero__media{position:absolute;inset:0;background:radial-gradient(ellipse at 70% 30%,#2a4592 0%,#17296a 40%,var(--navy-deep) 100%)}
.hero__nav{position:absolute;left:0;top:0;width:1200px;height:80px}
.logo{position:absolute;left:74px;top:22px;font-family:"Raleway",Arial,sans-serif;font-weight:600;font-size:26px;color:var(--white)}
.nav-links{position:absolute;left:557px;top:30px;display:flex;gap:0;font-size:14px;color:var(--white);font-weight:500}
.nav-links span{margin-right:30px}
.nav-phone{position:absolute;left:978px;top:28px;display:flex;align-items:center;gap:10px;color:var(--white);font-weight:600;font-size:15px}
.hero__headline{position:absolute;left:138px;top:326px;color:var(--white);font-family:"Barlow Condensed","Arial Narrow",sans-serif;font-weight:600;text-transform:uppercase}
.hero__headline .l1{font-size:40px;line-height:44px}
.hero__headline .l2{font-size:29px;line-height:34px}
.hero__headline em{font-style:normal;color:#8fbf3f}
.contact-card{position:absolute;left:793px;top:171px;width:331px;height:419px;background:var(--white);border-radius:6px;overflow:hidden;box-shadow:0 4px 18px rgba(0,0,0,.35)}
.contact-card__head{height:71px;background:var(--green);color:var(--white);font-family:"Barlow Condensed","Arial Narrow",sans-serif;font-weight:600;font-size:29px;text-align:center;line-height:71px}
.field{position:absolute;left:29px;width:276px;height:40px;background:var(--field);border-radius:2px;font-size:13px;color:var(--muted);padding-left:12px;line-height:40px}
.submit{position:absolute;left:29px;top:312px;width:276px;height:40px;background:var(--green);border-radius:2px;color:var(--white);text-align:center;line-height:40px;font-family:"Barlow Condensed","Arial Narrow",sans-serif;font-weight:600;font-size:17px}
.privacy{position:absolute;left:20px;top:362px;width:291px;text-align:center;font-size:12px;line-height:17px;color:#666}

/* buttons */
.btn-download{position:absolute;left:457px;width:286px;height:36px;border-radius:18px;background:var(--green);color:var(--white);font-family:"Barlow Condensed","Arial Narrow",sans-serif;font-weight:600;font-size:16px;display:flex;align-items:center;justify-content:center;gap:10px;text-transform:uppercase}

/* services */
.services{position:absolute;left:0;top:1643px;width:1200px;height:543px;border-bottom:1px solid var(--line)}
.section-title{position:absolute;left:0;width:1200px;text-align:center;font-family:"Barlow Condensed","Arial Narrow",sans-serif;font-weight:600;font-size:26px;color:var(--ink);text-transform:uppercase}
.services .section-title{top:48px}
.service{position:absolute;top:96px;width:330px;text-align:center}
.service--a{left:73px}.service--b{left:437px}.service--c{left:795px}
.service__divider{position:absolute;top:110px;width:1px;height:290px;background:var(--line)}
.service__icon{display:block;margin:0 auto}
.service__kicker{margin-top:56px;font-size:15px;color:#444}
.service__name{font-size:21px;color:var(--ink);font-weight:500;margin-top:2px}
.service__desc{margin:26px auto 0;width:280px;font-size:14px;line-height:22px;color:#555}
.services .btn-download{top:451px}

/* welcome */
.welcome{position:absolute;left:0;top:2186px;width:1200px;height:674px}
.welcome__title{position:absolute;left:74px;top:62px;font-family:"Barlow Condensed","Arial Narrow",sans-serif;font-weight:600;font-size:27px;color:var(--ink);text-transform:uppercase}
.welcome__body{position:absolute;left:74px;top:112px;width:478px}
.welcome__lead{font-size:16px;line-height:22px;color:#333;font-weight:600;margin-bottom:20px}
.welcome__body p{font-size:13.5px;line-height:20px;margin-bottom:20px}
.diagram{position:absolute;left:540px;top:0}

/* metrics */
.metrics{position:absolute;left:0;top:2860px;width:1200px;height:340px}
.chart{position:absolute;top:26px;background:var(--cream);border:1px solid #e6dcae}
.chart--growth{left:76px;width:191px;height:281px}
.chart--relative{left:295px;width:195px;height:281px}
.metrics__text{position:absolute;left:562px;top:24px;width:606px}
.metrics__text p{font-size:13.5px;line-height:20px;margin-bottom:20px}

/* closing */
.closing{position:absolute;left:0;top:3200px;width:1200px;height:288px}
.closing p{position:absolute;left:74px;width:1060px;font-size:13.5px;line-height:20px}
.closing .p1{top:60px}
.closing .p2{top:102px}
.closing .btn-download{top:214px}

/* footer */
.footer{position:absolute;left:0;top:3488px;width:1200px;height:83px;background:var(--footer);color:var(--white)}
.footer .logo{top:26px;font-size:22px}
.footer__legal{position:absolute;left:208px;top:33px;font-size:13px;color:#aab3cf}
</style>
</head>
<body>

<div class="board-label board-label--top">YES, IT IS POSSIBLE<br>PUT YOUR VIDEO IN BACKGROUND</div>
<svg class="board-arrow" width="16" height="34" viewBox="0 0 16 34"><path d="M8 0v30M2 24l6 8 6-8" fill="none" stroke="#2b2b2b" stroke-width="2"/></svg>

<!-- hero: video background variant -->
<section class="hero hero--showcase">
  <div class="hero__media" role="img" aria-label="Background video: hands operating a glowing digital interface in deep blue tones"></div>
  <div class="hero__nav">
    <div class="logo">Lanternby Works</div>
    <div class="nav-links"><span>Home</span><span>Book</span><span>Services</span><span>Downloadable Research</span></div>
    <div class="nav-phone"><svg width="14" height="20" viewBox="0 0 14 20"><rect x="1" y="1" width="12" height="18" rx="2" fill="none" stroke="#fff" stroke-width="2"/><circle cx="7" cy="15.5" r="1.2" fill="#fff"/></svg>1800 555 0142</div>
  </div>
  <div class="hero__headline"><div class="l1">We are a <em>consulting firm</em> that helps</div><div class="l2">companies thrive in the new digital era.</div></div>
  <form class="contact-card">
    <div class="contact-card__head">QUICK CONTACT</div>
    <div class="field" style="top:98px">First Name</div>
    <div class="field" style="top:151px">Last Name</div>
    <div class="field" style="top:204px">Email Address</div>
    <div class="field" style="top:257px">Organization</div>
    <div class="submit">SUBMIT</div>
    <div class="privacy">We respect your email privacy powered by<br>Mailwell Email Marketing</div>
  </form>
</section>

<div class="board-label board-label--home">HOMEPAGE DESIGN</div>

<!-- hero: homepage -->
<section class="hero hero--home">
  <div class="hero__media" role="img" aria-label="Photo: hands using a futuristic digital touch interface in deep blue tones"></div>
  <div class="hero__nav">
    <div class="logo">Lanternby Works</div>
    <div class="nav-links"><span>Home</span><span>Book</span><span>Services</span><span>Downloadable Research</span></div>
    <div class="nav-phone"><svg width="14" height="20" viewBox="0 0 14 20"><rect x="1" y="1" width="12" height="18" rx="2" fill="none" stroke="#fff" stroke-width="2"/><circle cx="7" cy="15.5" r="1.2" fill="#fff"/></svg>1800 555 0142</div>
  </div>
  <div class="hero__headline" style="top:336px"><div class="l1">We are a <em>consulting firm</em> that helps</div><div class="l2">companies thrive in the new digital era.</div></div>
  <form class="contact-card" style="top:186px">
    <div class="contact-card__head">QUICK CONTACT</div>
    <div class="field" style="top:98px">First Name</div>
    <div class="field" style="top:151px">Last Name</div>
    <div class="field" style="top:204px">Email Address</div>
    <div class="field" style="top:257px">Organization</div>
    <div class="submit">SUBMIT</div>
    <div class="privacy">We respect your email privacy powered by<br>Mailwell Email Marketing</div>
  </form>
</section>

<!-- services -->
<section class="services">
  <h2 class="section-title">Services we offer</h2>
  <div class="service__divider" style="left:421px"></div>
  <div class="service__divider" style="left:779px"></div>

  <div class="service service--a">
    <svg class="service__icon" width="90" height="90" viewBox="0 0 90 90"><circle cx="45" cy="45" r="42" fill="none" stroke="#e4e4e4" stroke-width="2"/><path d="M45 3a42 42 0 0 1 42 42" fill="none" stroke="#7a9a3d" stroke-width="3"/><rect x="39" y="28" width="12" height="22" rx="6" fill="none" stroke="#7a9a3d" stroke-width="2"/><path d="M34 44a11 11 0 0 0 22 0M45 55v8M39 63h12" fill="none" stroke="#7a9a3d" stroke-width="2"/></svg>
    <div class="service__kicker">Speaking</div>
    <div class="service__name">Engagements</div>
    <p class="service__desc">Provide an overview of the state of digital technology and implications for products, processes and customer journey.</p>
  </div>

  <div class="service service--b">
    <svg class="service__icon" width="90" height="90" viewBox="0 0 90 90"><circle cx="45" cy="45" r="42" fill="none" stroke="#e4e4e4" stroke-width="2"/><path d="M45 3a42 42 0 0 1 42 42" fill="none" stroke="#7a9a3d" stroke-width="3"/><rect x="34" y="27" width="22" height="30" rx="2" fill="none" stroke="#7a9a3d" stroke-width="2"/><path d="M39 35h12M39 41h12M39 47h8" stroke="#7a9a3d" stroke-width="2"/></svg>
    <div class="service__kicker">Digital</div>
    <div class="service__name">Assessment</div>
    <p class="service__desc">Help your company assess the state of your digital transformation.</p>
  </div>

  <div class="service service--c">
    <svg class="service__icon" width="90" height="90" viewBox="0 0 90 90"><circle cx="45" cy="45" r="42" fill="none" stroke="#e4e4e4" stroke-width="2"/><path d="M45 3a42 42 0 0 1 42 42" fill="none" stroke="#7a9a3d" stroke-width="3"/><path d="M32 58h28M35 58v-8h5v8M43 58v-13h5v13M51 58v-18h5v18M33 44l9-7 6 4 10-10" fill="none" stroke="#7a9a3d" stroke-width="2"/></svg>
    <div class="service__kicker">Digital</div>
    <div class="service__name">Strategy Development</div>
    <p class="service__desc">Based on the digital assessment and your objective, help define a digital vision and a strategy for implementation.</p>
  </div>

  <div class="btn-download"><svg width="18" height="18" viewBox="0 0 18 18"><circle cx="9" cy="9" r="8" fill="#fff"/><path d="M9 4.5v7M5.8 8.5 9 11.8l3.2-3.3" fill="none" stroke="#7a9a3d" stroke-width="1.8"/></svg>Download research worksheets</div>
</section>

<!-- welcome -->
<section class="welcome">
  <h2 class="welcome__title">Welcome to Lanternby Works Inc.</h2>
  <div class="welcome__body">
    <p class="welcome__lead">We are a consulting firm that helps companies thrive in the new digital era. A third digital era is emerging and established companies are in a position to win big in the new era.</p>
    <p>The first digital era started in the mid-fifties when companies began automating transactions and continued doing so for several decades. The second era emerged as the Internet became ingrained in the late nineties and early 2000's, when companies and customers went online, became mobile and embraced social.</p>
    <p>The third era is emerging now and is driven by such technologies as Internet of Things, machine learning, natural language processing (NLP), machine vision, and robotics. Companies are applying these technologies to revolutionize products, processes and the customer journey.</p>
    <p>We help companies establish their digital vision, understand current technologies, and how to put them to business use – making products smarter, operational processes more efficient, and the customer journey easier.</p>
  </div>

  <svg class="diagram" width="660" height="674" viewBox="0 0 660 674" role="group" aria-label="Business uses diagram">
    <g fill="var(--yellow)">
      <path d="M258 200 Q300 250 342 200 L342 508 Q300 458 258 508 Z"/>
      <path d="M140 522 Q196 564 140 606 L460 606 Q404 564 460 522 Z"/>
      <path d="M135 400 Q93 460 135 520 L60 520 Q93 460 60 400 Z" transform="translate(0 0)"/>
      <path d="M470 400 Q512 460 470 520 L545 520 Q512 460 545 400 Z"/>
    </g>
    <g fill="var(--green)" stroke="#fff" stroke-width="6">
      <circle cx="300" cy="145" r="72"/>
      <circle cx="93" cy="354" r="72"/>
      <circle cx="300" cy="354" r="72"/>
      <circle cx="512" cy="354" r="72"/>
      <circle cx="93" cy="564" r="72"/>
      <circle cx="300" cy="564" r="72"/>
      <circle cx="512" cy="564" r="72"/>
    </g>
    <g stroke="#222" stroke-width="2.5" fill="#222">
      <path d="M180 354h30"/><path d="M176 354l8-5v10z"/><path d="M214 354l-8-5v10z"/>
      <path d="M390 354h30"/><path d="M386 354l8-5v10z"/><path d="M424 354l-8-5v10z"/>
    </g>
    <g fill="#fff" font-family="Raleway, Arial, sans-serif" font-size="17" font-weight="500" text-anchor="middle">
      <text x="300" y="151">Vision</text>
      <text x="93" y="348">Digital</text><text x="93" y="369">Technology</text>
      <text x="300" y="348">Business</text><text x="300" y="369">Uses</text>
      <text x="512" y="348">Business</text><text x="512" y="369">Outcomes</text>
      <text x="93" y="570">Products</text>
      <text x="300" y="570">Processes</text>
      <text x="512" y="558">Customer</text><text x="512" y="579">Journey</text>
    </g>
  </svg>
</section>

<!-- metrics -->
<section class="metrics">
  <svg class="chart chart--growth" viewBox="0 0 191 281" role="img" aria-label="Bar chart: market cap growth, top half 18%, bottom half 12%">
    <text x="95" y="24" text-anchor="middle" font-family="Raleway, Arial, sans-serif" font-size="13" font-weight="600" fill="#333">Market Cap Growth</text>
    <g font-family="Raleway, Arial, sans-serif" font-size="9" fill="#555" text-anchor="end">
      <text x="34" y="49">20.0%</text><text x="34" y="71">18.0%</text><text x="34" y="93">16.0%</text><text x="34" y="115">14.0%</text><text x="34" y="137">12.0%</text><text x="34" y="159">10.0%</text><text x="34" y="181">8.0%</text><text x="34" y="203">6.0%</text><text x="34" y="225">4.0%</text><text x="34" y="247">2.0%</text><text x="34" y="269">0.0%</text>
    </g>
    <path d="M40 46v220h140" fill="none" stroke="#888" stroke-width="1"/>
    <rect x="62" y="68" width="28" height="198" fill="var(--green)"/>
    <rect x="126" y="134" width="28" height="132" fill="var(--green)"/>
    <g font-family="Raleway, Arial, sans-serif" font-size="10" fill="#333" text-anchor="middle"><text x="76" y="278">Top Half</text><text x="140" y="278">Bottom Half</text></g>
  </svg>

  <svg class="chart chart--relative" viewBox="0 0 195 281" role="img" aria-label="Bar chart: market cap growth relative to industry, top half +0.7%, bottom half -1.0%">
    <g font-family="Raleway, Arial, sans-serif" font-size="13" font-weight="600" fill="#333" text-anchor="middle"><text x="100" y="22">Market Cap Growth</text><text x="100" y="38">relative to Industry</text></g>
    <g font-family="Raleway, Arial, sans-serif" font-size="9" fill="#555" text-anchor="end">
      <text x="30" y="63">1.5%</text><text x="30" y="93">1.0%</text><text x="30" y="123">0.5%</text><text x="30" y="153">0.0%</text><text x="30" y="183">-0.5%</text><text x="30" y="213">-1.0%</text><text x="30" y="243">-1.5%</text><text x="30" y="268">-2.0%</text>
    </g>
    <path d="M36 60v205M36 150h148" fill="none" stroke="#888" stroke-width="1"/>
    <rect x="64" y="108" width="24" height="42" fill="var(--green)"/>
    <rect x="132" y="150" width="24" height="60" fill="var(--green)"/>
    <g font-family="Raleway, Arial, sans-serif" font-size="10" fill="#333" text-anchor="middle"><text x="76" y="166">Top Half</text><text x="144" y="140">Bottom Half</text></g>
  </svg>

  <div class="metrics__text">
    <p>We also monitor what companies are doing in the area of digital and the relationship of digital initiatives and business performance. We look at the level of digital activities the company mentions in their annual reports. We then segregate the more digitally active companies (top half) from the less digitally active companies (bottom half) and compare business metrics.</p>
    <p>For example, the chart below outlines that more digitally active companies (top half) achieved and average market cap growth per year of 18% from 2012 to 2015, whereas less digitally active companies (bottom half) increased market cap at an average of 12% per year.</p>
    <p>Isolating the impact of industry, since some industries increased market cap more than other industries shows that the top half companies grew market cap about 0.7% faster than their industry counterparts and bottom half companies grew market cap 1% less than their industry counterparts.</p>
  </div>
</section>

<!-- closing -->
<section class="closing">
  <p class="p1">You can read about these concepts, examples, and how to move your company forward in the new digital era in our book Leading Digital Forward.</p>
  <p class="p2">Peruse the content on this site, and feel free to download some of our research. We hope you will find it useful. Would you like to have a conversation about digital and your company? Complete the contact form on the right sidebar. We love talking about how established companies can win big in the new digital era!</p>
  <div class="btn-download"><svg width="18" height="18" viewBox="0 0 18 18"><circle cx="9" cy="9" r="8" fill="#fff"/><path d="M9 4.5v7M5.8 8.5 9 11.8l3.2-3.3" fill="none" stroke="#7a9a3d" stroke-width="1.8"/></svg>Download research worksheets</div>
</section>

<footer class="footer">
  <div class="logo">Lanternby Works</div>
  <div class="footer__legal">© 2017 Lanternby Works Inc. &nbsp;|&nbsp; Terms of Use &nbsp;|&nbsp; Privacy</div>
</footer>

</body>
</html>
```